NEW YORK Plumbing/utility company 10 year anniversary business card

Looking For simple back and front business card would like to include a few things in description
We offer 24/7 emergency service
residential
commercial
industrial
municipal
services offered
Plumbing
hydro excavation
hydro jetting
Well pumps
Sewer pumps
water mains
sewer mains

```html
<!DOCTYPE html>
<html lang="en">
<head>
<meta charset="utf-8">
<title>Kestrel Ridge Water &amp; Sewer – Business Card</title>
<link href="https://fonts.googleapis.com/css2?family=Montserrat:wght@400;500;600;700&display=swap" rel="stylesheet">
<style>
  :root {
    --bg: #a9bcb6;
    --navy: #1565a8;
    --sky: #1aa7e8;
    --grad-light: #00c3ec;
    --grad-dark: #0058a6;
    --ink: #4a4a4a;
    --ink-strong: #2b2b2b;
    --rule: #8a8a8a;
    --white: #ffffff;
  }
  * { margin: 0; padding: 0; box-sizing: border-box; }
  html, body {
    width: 1200px;
    height: 1029px;
    overflow: hidden;
    background: var(--bg);
    font-family: "Montserrat", Arial, sans-serif;
  }
  .canvas {
    position: relative;
    width: 1200px;
    height: 1029px;
    display: flex;
    flex-direction: column;
    align-items: center;
    justify-content: center;
    gap: 70px;
  }
  .card {
    width: 640px;
    height: 366px;
    border-radius: 4px;
    box-shadow: 0 14px 30px rgba(40, 60, 55, 0.28);
    position: relative;
    overflow: hidden;
  }

  /* Back side */
  .card-back {
    background: linear-gradient(135deg, var(--grad-light) 0%, var(--grad-dark) 100%);
    display: flex;
    align-items: center;
    justify-content: center;
  }
  .back-name {
    color: var(--white);
    font-weight: 700;
    text-transform: uppercase;
    text-align: center;
    line-height: 1.15;
    letter-spacing: 2px;
  }
  .back-name .line-main { display: block; font-size: 44px; }
  .back-name .line-sub { display: block; font-size: 24px; letter-spacing: 5px; margin-top: 6px; }

  /* Front side */
  .card-front {
    background: var(--white);
    display: flex;
    align-items: center;
    padding: 0 40px 0 56px;
  }
  .front-brand {
    flex: 0 0 250px;
    display: flex;
    align-items: center;
    gap: 12px;
  }
  .brand-mark {
    width: 20px;
    height: 20px;
    border-radius: 50%;
    background: var(--navy);
    flex: 0 0 auto;
  }
  .brand-name {
    color: var(--navy);
    font-weight: 700;
    text-transform: uppercase;
    line-height: 1.15;
  }
  .brand-name .line-main { display: block; font-size: 26px; letter-spacing: 1px; }
  .brand-name .line-sub { display: block; font-size: 14px; letter-spacing: 3px; margin-top: 4px; }

  .divider {
    width: 1px;
    height: 200px;
    background: var(--rule);
    margin: 0 22px 0 20px;
    flex: 0 0 auto;
  }
  .contact {
    color: var(--ink);
    font-size: 12px;
    line-height: 1.35;
  }
  .person-name {
    font-size: 20px;
    font-weight: 700;
    color: var(--navy);
    letter-spacing: 0.5px;
    line-height: 1.1;
  }
  .person-name .accent { color: var(--sky); }
  .person-role { font-size: 11px; margin: 2px 0 12px 10px; }
  .contact-lines { margin: 0 0 10px 20px; }
  .email { color: var(--navy); font-weight: 500; }
  .services { margin-left: 28px; }
  .services .emergency { color: var(--ink-strong); font-weight: 700; font-size: 13px; }
</style>
</head>
<body>
<main class="canvas">
  <section class="card card-back" aria-label="Card back">
    <p class="back-name">
      <span class="line-main">Kestrel Ridge</span>
      <span class="line-sub">Water &amp; Sewer</span>
    </p>
  </section>

  <section class="card card-front" aria-label="Card front">
    <div class="front-brand">
      <span class="brand-mark" aria-hidden="true"></span>
      <p class="brand-name">
        <span class="line-main">Kestrel Ridge</span>
        <span class="line-sub">Water &amp; Sewer</span>
      </p>
    </div>
    <div class="divider" aria-hidden="true"></div>
    <div class="contact">
      <p class="person-name">YOUR <span class="accent">NAME</span></p>
      <p class="person-role">Managing Director</p>
      <div class="contact-lines">
        <p>845-555-0182</p>
        <p class="email">info@kestrelridgeny.com</p>
      </div>
      <div class="services">
        <p>Plumbing-Hydro excavation</p>
        <p>Hydro jetting-Well pumps</p>
        <p>Sewer pumps-Water mains</p>
        <p>Sewer mains</p>
        <p class="emergency">24/7 emergency services</p>
        <p>Residential-Commercial</p>
        <p>Industrial-Municipal</p>
      </div>
    </div>
  </section>
</main>
</body>
</html>
```